Redesign vek7.ch agency website for unique design with speed and conversion

We want to redesign our website vek7.ch. Our omnichannel marketing agency builds webshops and integrates them into existing systems like ERP/CRM and supports with online marketing campaigns like plimtor ads and social media. The target of the redesign is to get a great look and feel for customers to see directly what we do, (please design something for our three focus areas eCommerce, Online marketing and Integration)
and to improve the pages speed drastically for SEO. Please see our attachment.
Target Market(s)
B2B
Industry/Entity Type
eCommerce Agency
Coding
Coded - Design and coding required
Number of Pages Required
5+ page
Look and feel
Each slider illustrates characteristics of the customer's brand and the style your logo design should communicate.

```html
<!DOCTYPE html>
<html lang="en">
<head>
<meta charset="utf-8">
<title>VEK7 – Online marketing agency</title>
<link rel="stylesheet" href="https://fonts.googleapis.com/css2?family=Poppins:ital,wght@0,300;0,400;0,500;0,600;1,400&display=swap">
<style>
:root{
  --green:#0be34a;
  --mint:#8ff0a8;
  --ink:#161616;
  --dark:#0b0b0b;
  --muted:#5a5f63;
  --pale:#f0f7fa;
  --white:#fff;
}
*{box-sizing:border-box;margin:0;padding:0}
html,body{width:1200px;height:4415px;overflow:hidden;background:#fff}
body{font-family:"Poppins",sans-serif;color:var(--ink);position:relative}
.section{position:absolute;left:0;width:1200px}
.abs{position:absolute}
.photo{position:absolute;display:block}
.eyebrow{font-size:12px;color:var(--green);font-weight:500}
.h2{font-size:27px;font-weight:400;line-height:1.3}
.body{font-size:12px;color:var(--muted);line-height:1.55}
.btn{position:absolute;height:30px;border-radius:15px;font-size:10px;font-weight:600;display:flex;align-items:center;justify-content:center}
.btn-solid{background:var(--green);color:#fff}
.btn-line{border:2px solid var(--green);color:var(--green);background:#fff}

/* header */
.header{top:0;height:70px;background:var(--dark)}
.logo{font-weight:600;color:var(--green);font-size:34px;letter-spacing:2px}
.nav{left:260px;top:25px;display:flex;gap:28px;font-size:11px;color:#ddd}
.nav .active{color:var(--green)}
.phone{left:672px;top:25px;font-size:10px;color:#ddd;display:flex;gap:6px;align-items:center}
.contact-btn{left:870px;top:18px;width:88px;height:34px;border:2px solid var(--green);border-radius:17px;color:var(--green);font-size:10px;display:flex;align-items:center;justify-content:center}
.lang{left:968px;top:18px;width:34px;height:34px;border:2px solid #fff;border-radius:50%;color:#fff;font-size:10px;font-weight:600;display:flex;align-items:center;justify-content:center}

/* hero */
.hero{top:70px;height:435px;background:linear-gradient(120deg,#2a3a3e,#45575a 45%,#1e2628)}
.hero h1{position:absolute;left:150px;top:80px;width:560px;font-size:33px;font-weight:400;color:#fff;line-height:1.3}
.hero p{position:absolute;left:150px;top:190px;width:460px;font-size:13px;color:#e8e8e8;line-height:1.4}
.arrows{left:150px;top:385px;display:flex;gap:6px}
.arrows span{width:24px;height:24px;border:1.5px solid #ccc;border-radius:50%;display:flex;align-items:center;justify-content:center;color:#ddd;font-size:11px}
.tabs{left:610px;top:377px;width:590px;height:58px;background:#fff;display:flex}
.tab{flex:1;padding:14px 0 0 55px;font-size:10px;line-height:1.5}
.tab.on{background:var(--green);color:#fff}

/* about */
.about{top:505px;height:476px}
.about h2{position:absolute;left:610px;top:126px;width:300px}
.about .body{position:absolute;left:610px;top:250px;width:280px;font-size:12.5px}
.more{position:absolute;left:610px;top:350px;border-left:2px solid var(--green);padding-left:12px;font-size:10px;height:26px;display:flex;align-items:center}

/* values */
.values{top:981px;height:144px;background:var(--green);display:flex;padding:0 200px}
.value{flex:1;display:flex;flex-direction:column;align-items:center;justify-content:center;gap:10px;color:#0a4d1e;font-size:11px;border-right:1px solid rgba(0,0,0,.12)}
.value:last-child{border:none}

/* features */
.feature{height:374px}
.feature .band{position:absolute;left:0;right:0;top:58px;bottom:0;background:var(--pale)}
.feature h2{position:absolute;width:300px}
.feature .body{position:absolute;width:290px;font-size:9.5px}

/* testimonials */
.clients{top:2245px;height:420px}
.quote{font-size:10.5px;font-style:italic;line-height:1.7;width:270px}
.dot{position:absolute;border-radius:50%;background:#c9cdd0}

/* team */
.team{top:2800px;height:425px}
.card-name{font-size:10px;font-weight:600}
.card-role{font-size:7px;color:var(--muted)}
.partners{left:220px;top:320px;width:760px;height:74px;background:#fff;box-shadow:0 4px 16px rgba(0,0,0,.1);display:flex;align-items:center;justify-content:space-around}
.partners span{width:80px;height:26px;border-radius:4px;background:#d7dbde}

/* articles */
.articles{top:3225px;height:430px}
.article{position:absolute;top:80px;width:188px;height:262px;border-bottom:3px solid var(--green)}
.article .date{font-size:7px;color:var(--green);margin:18px 0 0 18px}
.article .title{font-size:10px;font-weight:500;margin:8px 18px 0;line-height:1.5}
.article .read{font-size:7px;color:var(--green);margin:16px 0 0 18px}

/* contact */
.contact{top:3660px;height:450px;background:linear-gradient(90deg,#1c2228,#2d353c 50%,#1c2228)}
.contact h2{position:absolute;top:50px;width:1200px;text-align:center;color:#fff;font-size:24px;font-weight:400}
.c-item{position:absolute;top:110px;width:150px;text-align:center;color:#fff;font-size:8px;line-height:1.5}
.c-item .ring{width:46px;height:46px;border:2px solid var(--green);border-radius:50%;margin:0 auto 12px;display:flex;align-items:center;justify-content:center}
.field{position:absolute;height:24px;border-radius:12px;background:#fff;font-size:8px;padding:6px 16px;color:#333}

/* footer */
.footer{top:4110px;height:305px;background:#f3f9fb}
.col{position:absolute;top:55px;font-size:8px;line-height:2;color:#333}
.col b{font-size:10px;font-weight:500;display:block;margin-bottom:10px}
.social{position:absolute;left:980px;width:24px;height:24px;border:2px solid var(--green);border-radius:50%}
</style>
</head>
<body>

<header class="section header">
  <div class="abs logo" style="left:70px;top:12px">VEK7</div>
  <nav class="abs nav"><span class="active">Home</span><span>eCommerce</span><span>Online Marketing</span><span>Integration</span><span>Company ⌄</span></nav>
  <div class="abs phone">
    <svg width="10" height="10" viewBox="0 0 24 24"><path d="M6 2l4 4-2 3c1 3 4 6 7 7l3-2 4 4-3 4C10 22 2 14 2 5z" fill="#0be34a"/></svg>+41 44 000 12 34</div>
  <div class="abs contact-btn">Contact Us</div>
  <div class="abs lang">EN</div>
</header>

<section class="section hero">
  <div class="photo" role="img" aria-label="Team working on laptops with analytics charts" style="inset:0;background:linear-gradient(120deg,rgba(40,60,64,.6),rgba(20,28,30,.4))"></div>
  <h1>Your online marketing agency in zurich for SMEs</h1>
  <p>You want to reach the right people online and more generate sales. contact us!</p>
  <div class="btn btn-solid" style="left:150px;top:252px;width:140px">Make an Appointment Now</div>
  <div class="abs arrows"><span>‹</span><span>›</span></div>
  <div class="abs tabs">
    <div class="tab">01.<br>eCommerce</div>
    <div class="tab on">02.<br>Online Marketing</div>
    <div class="tab">03.<br>Integration</div>
  </div>
</section>

<section class="section about">
  <div class="photo" role="img" aria-label="Agency employee holding a laptop with the company sticker" style="left:200px;top:56px;width:314px;height:362px;background:linear-gradient(160deg,#2a3a55,#3a7fa8 55%,#7fb6b0)"></div>
  <div class="abs eyebrow" style="left:610px;top:95px;font-size:9px">About the VEK7</div>
  <h2 class="h2">We have many years of experience in software consulting.</h2>
  <p class="body">Our goal is to achieve the goals of our customers in a short time. we create added value and implement demanding requirements.</p>
  <div class="more">More About Our Company →</div>
</section>

<section class="section values">
  <div class="value">
    <svg width="44" height="44" viewBox="0 0 44 44" fill="none" stroke="#0a4d1e" stroke-width="1.6"><rect x="8" y="22" width="28" height="18"/><path d="M14 22V12h16v10M22 4v8M18 30h8"/></svg>Sustainability</div>
  <div class="value">
    <svg width="44" height="44" viewBox="0 0 44 44" fill="none" stroke="#0a4d1e" stroke-width="1.6"><circle cx="22" cy="18" r="12"/><circle cx="22" cy="18" r="6"/><path d="M15 28l-3 12 10-5 10 5-3-12"/></svg>Quality</div>
  <div class="value">
    <svg width="44" height="44" viewBox="0 0 44 44" fill="none" stroke="#0a4d1e" stroke-width="1.6"><circle cx="12" cy="12" r="4"/><circle cx="22" cy="10" r="4"/><circle cx="32" cy="12" r="4"/><path d="M4 40V24h36v16M12 24v16M22 24v16M32 24v16"/></svg>Customer Orientation</div>
</section>

<section class="section feature" style="top:1125px">
  <div class="band"></div>
  <div class="photo" role="img" aria-label="Laptop showing a webshop on a wooden desk" style="left:610px;top:0;width:390px;height:302px;background:linear-gradient(150deg,#d8d6d0,#9a8f80 60%,#5c5246)"></div>
  <h2 class="h2" style="left:200px;top:130px;font-size:24px">Your successful entry into Ecommerce</h2>
  <p class="body" style="left:200px;top:210px">Do you want to sell your products or services online? But as an SME, don't you have a marketing department with e-commerce know-how? Then you will face a series of questions essential to the success of your web business crucial are ...</p>
  <div class="btn btn-solid" style="left:200px;top:290px;width:98px;height:26px">Explore More</div>
</section>

<section class="section feature" style="top:1499px">
  <div class="band"></div>
  <div class="photo" role="img" aria-label="Tablet with online marketing notes and glasses on a desk" style="left:200px;top:0;width:390px;height:302px;background:linear-gradient(150deg,#c98a5a,#e4ddd2 55%,#8a6a4a)"></div>
  <h2 class="h2" style="left:610px;top:130px;font-size:24px">Our individual online marketing solutions</h2>
  <p class="body" style="left:610px;top:210px">In us you will find a dedicated team with passion, expertise and curiosity for all topics related to e-commerce and online marketing. Our Agency brings you quickly, purposefully and economically with your products online.</p>
  <div class="btn btn-line" style="left:610px;top:288px;width:98px;height:28px">Explore More</div>
</section>

<section class="section feature" style="top:1873px">
  <div class="band"></div>
  <div class="photo" role="img" aria-label="Hands joining coloured puzzle pieces in black and white" style="left:610px;top:0;width:390px;height:302px;background:linear-gradient(150deg,#3a3a3a,#9a9a9a 50%,#2a2a2a)"></div>
  <h2 class="h2" style="left:200px;top:130px;font-size:24px">Lorem ipsum is simply integration dummy</h2>
  <p class="body" style="left:200px;top:210px">Sed ut perspiciatis unde omnis iste natus error sit voluptatem laorem accusantium doloremque laudantium, totam rem aperiam, eaque ipsa quae ab illo inventore veritatis et quasi architecto beatae vitae dicta sunt explicabo. Nemo enim ipsam voluptatem ...</p>
  <div class="btn btn-line" style="left:200px;top:288px;width:98px;height:28px">Explore More</div>
</section>

<section class="section clients">
  <h2 class="h2 abs" style="left:200px;top:60px;font-size:24px">What clients say</h2>
  <svg class="abs" style="left:200px;top:125px" width="30" height="22" viewBox="0 0 30 22"><path d="M2 20c0-10 4-16 10-18M16 20c0-10 4-16 10-18" stroke="#0be34a" stroke-width="3" fill="none"/></svg>
  <div class="abs quote" style="left:200px;top:165px"><b style="font-weight:600">Thank you for the really successful website.</b><br>It fully meets my expectations. The cooperation was professional and uncomplicated. Again any time. Already have several positive feedbacks for the get page.</div>
  <div class="abs" style="left:200px;top:290px;font-size:8px;font-weight:600">Mara Lenz</div>
  <div class="abs" style="left:200px;top:304px;font-size:6.5px;color:var(--muted)">owner of Praxis Nordlicht therapy and speech care</div>
  <div class="abs" style="left:200px;top:325px;display:flex;gap:4px"><i class="dot" style="position:static;width:6px;height:6px;background:#ccc"></i><i class="dot" style="position:static;width:6px;height:6px;background:var(--green)"></i><i class="dot" style="position:static;width:6px;height:6px;background:#ccc"></i><i class="dot" style="position:static;width:6px;height:6px;background:#ccc"></i><i class="dot" style="position:static;width:6px;height:6px;background:#ccc"></i></div>
  <div class="dot" style="left:655px;top:125px;width:130px;height:130px;background:#eef1f3"></div>
  <div class="photo" role="img" aria-label="Portrait of client" style="left:670px;top:140px;width:100px;height:100px;border-radius:50%;background:linear-gradient(160deg,#e5e7e9,#8c9298)"></div>
  <div class="dot" role="img" aria-label="Client portrait" style="left:740px;top:30px;width:32px;height:32px"></div>
  <div class="dot" role="img" aria-label="Client portrait" style="left:840px;top:75px;width:20px;height:20px"></div>
  <div class="dot" role="img" aria-label="Client portrait" style="left:800px;top:160px;width:24px;height:24px"></div>
  <div class="dot" role="img" aria-label="Client portrait" style="left:855px;top:218px;width:40px;height:40px"></div>
  <div class="dot" role="img" aria-label="Client portrait" style="left:750px;top:265px;width:20px;height:20px"></div>
  <div class="abs" style="left:220px;right:220px;top:395px;border-top:1px solid #e6e9eb"></div>
</section>

<section class="section team">
  <div class="abs" style="left:0;right:0;top:58px;height:300px;background:var(--mint)"></div>
  <h2 class="h2 abs" style="left:370px;top:0;font-size:22px">Our team</h2>
  <div class="photo" role="img" aria-label="Portrait of Jonas Keller, eCommerce Manager" style="left:370px;top:58px;width:220px;height:248px;background:linear-gradient(160deg,#e6e6e4,#b8b8b4)"></div>
  <div class="abs" style="left:370px;top:256px;width:170px;height:50px;background:var(--mint);padding:10px 14px">
    <div class="card-name">Jonas Keller</div><div class="card-role">eCommerce Manager</div></div>
  <div class="abs" style="left:500px;top:270px;width:20px;height:20px;border:1.5px solid #222;border-radius:50%"></div>
  <div class="photo" role="img" aria-label="Portrait of Lukas Brand, Online Marketing Manager" style="left:610px;top:0;width:220px;height:262px;background:linear-gradient(160deg,#e8e8e6,#b4b6b8)"></div>
  <div class="abs" style="left:610px;top:210px;width:170px;height:52px;background:var(--mint);padding:10px 14px">
    <div class="card-name">Lukas Brand</div><div class="card-role">Online Marketing Manager</div></div>
  <div class="abs" style="left:745px;top:225px;width:20px;height:20px;border:1.5px solid #222;border-radius:50%"></div>
  <div class="abs" style="left:610px;top:278px;border-left:2px solid var(--green);padding-left:12px;height:22px;font-size:8px;display:flex;align-items:center">Explore More →</div>
  <div class="abs partners" role="img" aria-label="Partner badges"><span></span><span></span><span></span><span></span><span></span><span></span></div>
</section>

<section class="section articles">
  <h2 class="h2 abs" style="top:0;width:1200px;text-align:center;font-size:22px">Recent articles</h2>
  <div class="article" style="left:200px">
    <div class="photo" role="img" aria-label="Man writing on a whiteboard" style="position:relative;height:115px;background:linear-gradient(150deg,#e8ebec,#b0b4b0)"></div>
    <div class="date">JULY 10 2023</div><div class="title">There are many variations lorem Ipsum available, literature</div><div class="read">Read More →</div></div>
  <div class="article" style="left:406px">
    <div class="photo" role="img" aria-label="Hands typing on a laptop" style="position:relative;height:115px;background:linear-gradient(150deg,#c6ccd2,#5a6470)"></div>
    <div class="date">SEP 10 2023</div><div class="title">There are many variations lorem Ipsum available, literature</div><div class="read">Read More →</div></div>
  <div class="article" style="left:612px">
    <div class="photo" role="img" aria-label="Team meeting in a bright office" style="position:relative;height:115px;background:linear-gradient(150deg,#d8dde0,#7a8890)"></div>
    <div class="date">JAN 10 2023</div><div class="title">There are many variations lorem Ipsum available, literature</div><div class="read">Read More →</div></div>
  <div class="btn btn-line" style="left:562px;top:372px;width:76px;height:24px;font-size:8px">View All</div>
</section>

<section class="section contact">
  <div class="photo" role="img" aria-label="Two team members standing on either side, darkened" style="inset:0;background:linear-gradient(90deg,rgba(60,70,80,.5),rgba(20,24,28,.2) 50%,rgba(60,70,80,.5))"></div>
  <h2>Contact us</h2>
  <div class="c-item" style="left:375px"><div class="ring"><svg width="18" height="18" viewBox="0 0 24 24" fill="none" stroke="#0be34a" stroke-width="2"><path d="M12 22s7-7 7-12a7 7 0 0 0-14 0c0 5 7 12 7 12z"/><circle cx="12" cy="10" r="2.5"/></svg></div>Lindenweg 12, 8000 Zurich,<br>Switzerland</div>
  <div class="c-item" style="left:525px"><div class="ring"><svg width="18" height="18" viewBox="0 0 24 24" fill="none" stroke="#0be34a" stroke-width="2"><path d="M6 2l4 4-2 3c1 3 4 6 7 7l3-2 4 4-3 4C10 22 2 14 2 5z"/></svg></div>Phone:<br>+41 44 000 12 34</div>
  <div class="c-item" style="left:675px"><div class="ring"><svg width="18" height="18" viewBox="0 0 24 24" fill="none" stroke="#0be34a" stroke-width="2"><rect x="3" y="5" width="18" height="14"/><path d="M3 5l9 8 9-8"/></svg></div>Email:<br>info@vek7.ch</div>
  <div class="field" style="left:228px;top:215px;width:142px">Name</div>
  <div class="field" style="left:385px;top:215px;width:142px">Email</div>
  <div class="field" style="left:542px;top:215px;width:142px">Phone</div>
  <div class="field" style="left:228px;top:250px;width:456px;height:98px;border-radius:4px">Type your Message ...</div>
  <div class="btn" style="left:417px;top:372px;width:80px;height:22px;border:2px solid var(--green);color:var(--green);font-size:8px">Send</div>
</section>

<footer class="section footer">
  <div class="abs logo" style="left:200px;top:40px">VEK7</div>
  <div class="col" style="left:398px"><b>Useful links</b>Online stores and websites<br>SEO - search engine optimization<br>SEA - Plimtor Ads<br>The social media agency from Zurich<br>Privacy<br>Imprint</div>
  <div class="col" style="left:576px"><b>Quick links</b>Home<br>eCommerce<br>Online Marketing<br>Integration</div>
  <div class="col" style="left:758px"><b>Company</b>About Us<br>Blog<br>Contact Us<br>History<br>Customer References</div>
  <div class="social" style="top:45px"></div>
  <div class="social" style="top:75px;background:var(--green)"></div>
  <div class="social" style="top:105px"></div>
  <div class="abs" style="left:200px;top:250px;font-size:7px">© 2023 <span style="color:var(--green)">VEK7 Marketing GmbH</span>. All Right Reserved</div>
  <svg class="abs" style="left:962px;top:242px" width="16" height="20" viewBox="0 0 16 20"><path d="M8 0l8 20-8-5-8 5z" fill="#0be34a"/></svg>
</footer>

</body>
</html>
```